Software engineering company needs business card

I need a cool business card. Company: Belan Works Brindlewood Ave 41 58207 Marrowfield Name: Gerald Vanholt CEO / Managing Director & Owner

```html
<!DOCTYPE html>
<html lang="de">
<head>
<meta charset="utf-8">
<title>Belan Works – Visitenkarte</title>
<link rel="stylesheet" href="https://fonts.googleapis.com/css2?family=Nunito+Sans:wght@300;600;700&display=swap">
<style>
  :root {
    --page-bg: #fdfdfd;
    --card-top-a: #333333;
    --card-top-b: #4a4a48;
    --card-panel-a: #2c2c2c;
    --card-panel-b: #444443;
    --card-shade: #1c1c1c;
    --brand-green: #8dbb3f;
    --pattern-grey: #a9a9a9;
    --text-light: #ffffff;
  }
  html, body {
    margin: 0;
    width: 1200px;
    height: 1200px;
    overflow: hidden;
    background: var(--page-bg);
    font-family: "Nunito Sans", sans-serif;
  }
  .business-card {
    position: absolute;
    left: 214px;
    top: 384px;
    width: 786px;
    height: 446px;
    overflow: hidden;
  }
  .card-shapes {
    position: absolute;
    inset: 0;
    width: 100%;
    height: 100%;
    display: block;
  }
  .brand {
    position: absolute;
    left: 0;
    width: 500px;
    top: 118px;
    display: flex;
    justify-content: center;
    align-items: center;
    gap: 14px;
  }
  .brand-mark {
    width: 22px;
    height: 22px;
    background: var(--brand-green);
  }
  .brand-name {
    color: var(--text-light);
    font-weight: 600;
    font-size: 38px;
    letter-spacing: 3px;
    line-height: 1;
    white-space: nowrap;
  }
  .contact {
    position: absolute;
    right: 38px;
    top: 260px;
    text-align: right;
    color: var(--text-light);
    font-size: 21px;
    line-height: 26px;
    white-space: nowrap;
  }
  .contact-address {
    font-weight: 700;
    margin: 0 0 27px;
  }
  .contact-person {
    font-weight: 300;
    margin: 0;
  }
</style>
</head>
<body>
  <div class="business-card">
    <svg class="card-shapes" viewBox="0 0 916 520" preserveAspectRatio="none">
      <defs>
        <linearGradient id="topPlane" x1="0" y1="0" x2="1" y2="0">
          <stop offset="0" stop-color="var(--card-top-a)"/>
          <stop offset="1" stop-color="var(--card-top-b)"/>
        </linearGradient>
        <linearGradient id="sidePanel" x1="0" y1="1" x2="1" y2="0">
          <stop offset="0" stop-color="var(--card-panel-b)"/>
          <stop offset="0.4" stop-color="var(--card-panel-a)"/>
          <stop offset="1" stop-color="var(--card-panel-a)"/>
        </linearGradient>
        <linearGradient id="patternFill" x1="0" y1="0" x2="1" y2="0">
          <stop offset="0" stop-color="var(--brand-green)"/>
          <stop offset="0.5" stop-color="var(--pattern-grey)"/>
          <stop offset="1" stop-color="var(--brand-green)"/>
        </linearGradient>
      </defs>
      <rect class="card-base" width="916" height="520" fill="var(--card-shade)"/>
      <polygon class="upper-plane" points="0,0 916,0 916,158 176,355 0,268" fill="url(#topPlane)"/>
      <polygon class="shadow-fold" points="0,268 176,355 550,256 512,330 0,462" fill="var(--card-shade)"/>
      <polygon class="pattern-band" role="img" aria-label="Decorative band of repeated brand letters in green and grey" points="0,462 512,330 412,520 0,520" fill="url(#patternFill)"/>
      <polygon class="contact-panel" points="550,256 916,158 916,520 412,520" fill="url(#sidePanel)"/>
    </svg>

    <div class="brand">
      <span class="brand-mark"></span>
      <span class="brand-name">Belan Works</span>
    </div>

    <div class="contact">
      <p class="contact-address">Brindlewood Ave 41<br>58207 Marrowfield</p>
      <p class="contact-person">Gerald Vanholt<br>CEO / Geschäftsführer &amp; Inhaber</p>
    </div>
  </div>
</body>
</html>
```